Corportate Power Point Template

We need a corporate PPT Design for our startup Big Data company.

Basically, our company will ingest, analyze and generate dynamic Dashboards with data consumed from different sources like Social Networks, Enterprise Legacy Systems such as e-Commerce, ERP, CRM and others.

Company is headquartered in Brazil, but will have a global presence.

Industry/Entity Type

It Company

```html
<!DOCTYPE html>
<html lang="en">
<head>
<meta charset="utf-8">
<title>Project Title Here – Team Profile</title>
<link rel="stylesheet" href="https://fonts.googleapis.com/css2?family=Play:wght@400;700&family=Roboto+Condensed:wght@400&display=swap">
<style>
  :root {
    --orange: #f07a2c;
    --orange-soft: #f5b78a;
    --ink: #1e1e1e;
    --title-grey: #3a3a3a;
    --frame-border: #c9c9c9;
    --rule: #e2dcd6;
    --bg-top: #fdf6f0;
    --bg-bottom: #ffffff;
  }
  * { margin: 0; padding: 0; box-sizing: border-box; }
  html, body { width: 1200px; height: 900px; overflow: hidden; }
  body {
    position: relative;
    font-family: "Play", sans-serif;
    color: var(--ink);
    background: linear-gradient(160deg, var(--bg-top) 0%, var(--bg-bottom) 55%, #fbf7f3 100%);
  }
  .slide-title {
    position: absolute; left: 0; top: 27px; height: 81px;
    display: flex; align-items: center;
  }
  .slide-title__bar { width: 12px; height: 81px; background: var(--orange); }
  .slide-title__text {
    margin-left: 22px; font-size: 50px; font-weight: 700; letter-spacing: 0.5px;
    color: var(--title-grey);
  }
  .slide-title__text em { font-style: normal; color: var(--orange); }

  .portrait {
    position: absolute; left: 50px; top: 186px; width: 343px; height: 474px;
    background: #fff; border: 1.5px solid var(--frame-border);
    display: flex; align-items: center; justify-content: center;
  }
  .portrait__hint { font-size: 21px; font-weight: 700; color: var(--orange-soft); letter-spacing: 0.5px; }
  .portrait__tabs { position: absolute; left: 50px; top: 656px; }

  .profile-name {
    position: absolute; left: 50px; top: 669px; width: 343px; height: 51px;
    background: var(--orange); color: #fff; font-size: 30px;
    padding-left: 18px; line-height: 51px;
  }
  .profile-role { position: absolute; left: 65px; top: 727px; font-size: 27px; }

  .bio {
    position: absolute; left: 447px; top: 188px; width: 694px;
    font-size: 20px; line-height: 30px; text-align: justify;
  }
  .bio p + p { margin-top: 31px; }
  .contact { position: absolute; left: 447px; top: 635px; font-size: 20px; line-height: 42px; }
  .contact dt { display: inline; color: var(--orange); font-weight: 700; font-family: "Play", sans-serif; }
  .contact dd { display: inline; }

  .footer-rule { position: absolute; left: 0; right: 0; top: 817px; height: 1.5px; background: var(--rule); }
  .presenter {
    position: absolute; left: 12px; top: 853px;
    font-family: "Roboto Condensed", sans-serif; font-size: 21px;
  }
  .presenter span { color: var(--orange); }
  .brand {
    position: absolute; right: 15px; top: 838px; display: flex; align-items: center; gap: 10px;
    font-size: 36px; font-weight: 400; color: var(--orange);
  }
  .brand__mark { width: 22px; height: 22px; background: var(--orange); }
</style>
</head>
<body>
  <header class="slide-title">
    <div class="slide-title__bar"></div>
    <h1 class="slide-title__text"><em>Project</em> Title Here</h1>
  </header>

  <div class="portrait" role="img" aria-label="Portrait photo of the technical director">
    <span class="portrait__hint">IMAGE HERE DIRECTOR</span>
  </div>
  <svg class="portrait__tabs" width="343" height="14" viewBox="0 0 343 14" aria-hidden="true">
    <polygon points="6,13 22,0 38,13" fill="#f07a2c"/>
    <rect x="48" y="2" width="60" height="3" fill="#333"/>
    <rect x="115" y="2" width="90" height="3" fill="#333"/>
    <rect x="212" y="2" width="90" height="3" fill="#333"/>
  </svg>
  <div class="profile-name">Marco Vilela</div>
  <div class="profile-role">Technical Director</div>

  <section class="bio">
    <p>Marco Vilela has more than 14 years of experience in the IT industry. He has devoted much of his career to becoming a recognized expert in Keltrovan enterprise technologies and software architectures, most specifically in relation to DeskWeave, Keltrovan Tablestore and Postrelay Server.</p>
    <p>As Ostrivane Technical Director, Marco Vilela oversees development and implementation of strategic IT initiatives and best practices for enterprise clients as well as internally.</p>
    <p>He is particularly adept at applying his deep technical knowledge to large and complex projects and is the senior technical mentor for Farrowind’s Keltrovan infrastructure practice. He is involved in all aspects of Farrowind’s professional service lifecycle including business development, operations, pre-sales and consulting.</p>
  </section>

  <dl class="contact">
    <div><dt>Email :</dt> <dd>marco.vilela@ostrivane.com</dd></div>
    <div><dt>Fax :</dt> <dd>(001) 004-275190</dd></div>
  </dl>

  <div class="footer-rule"></div>
  <div class="presenter">Persentatator Name : <span>Lucas Ferraz</span></div>
  <div class="brand"><span class="brand__mark"></span>Ostrivane</div>
</body>
</html>
```